BrimFalcon Business Cards

We have a defined brand. Please visit our website to get a feel for the product and the color pallets. www.brimfalcon-demo.com

We need an updated, world class business card design. (See the attached existing card design). Please utilize BOTH sides of the card as shown and be creative with the layout. I do want the horse head icon to be positioned as it is with the existing card.

The remainder of the layout can be customized and I also want it vertically oriented.

Attached are the logo files and please use the colors as follows:
Green - #A5CE39
Tan - #CDBD99
Black

Feel free to play with the colors.

```html
<!DOCTYPE html>
<html lang="en">
<head>
<meta charset="utf-8">
<title>BrimFalcon Business Cards</title>
<link rel="stylesheet" href="https://fonts.googleapis.com/css2?family=Montserrat:wght@400;500;700&display=swap">
<style>
  :root {
    --backdrop: #1d1d1e;
    --card: #2e2e30;
    --green: #a5ce39;
    --green-deep: #6fae2e;
    --text: #f2f2f2;
    --muted: #8a8a8d;
    --art-dark: #1c1c1d;
    --art-light: #48484b;
  }
  * { margin: 0; padding: 0; box-sizing: border-box; }
  html, body { width: 1200px; height: 1108px; overflow: hidden; }
  body {
    background: var(--backdrop);
    font-family: "Montserrat", sans-serif;
    color: var(--text);
    display: flex;
    align-items: center;
    justify-content: center;
    gap: 90px;
  }
  .card {
    position: relative;
    width: 380px;
    height: 620px;
    background: var(--card);
    border-radius: 26px;
    border-bottom: 5px solid var(--green);
    border-right: 3px solid var(--green);
    overflow: hidden;
  }
  /* Front */
  .front-art {
    position: absolute;
    left: 20px; bottom: 30px;
    width: 300px; height: 300px;
    border-radius: 50%;
    background: radial-gradient(circle at 62% 40%, var(--art-light) 0%, #2a2a2c 45%, var(--art-dark) 100%);
  }
  .front-wordmark {
    position: absolute;
    right: 40px; top: 150px;
    writing-mode: vertical-rl;
    transform: rotate(180deg);
    font-size: 40px;
    font-weight: 500;
    letter-spacing: 1px;
    color: var(--muted);
    white-space: nowrap;
  }
  /* Back */
  .back { display: flex; flex-direction: column; align-items: center; text-align: center; padding: 78px 24px 0; }
  .brand { display: flex; align-items: center; gap: 10px; }
  .brand-dot { width: 34px; height: 34px; border-radius: 50%; background: var(--text); flex: none; }
  .brand-name { font-size: 28px; font-weight: 700; color: var(--text); white-space: nowrap; }
  .tagline { margin-top: 8px; font-size: 12px; letter-spacing: 3px; color: var(--text); white-space: nowrap; }
  .person-name { margin-top: 60px; font-size: 24px; font-weight: 700; letter-spacing: 1px; color: var(--green); text-transform: uppercase; }
  .person-title { margin-top: 6px; font-size: 16px; }
  .contact-icons { margin-top: 68px; display: flex; gap: 14px; }
  .contact-icons svg { width: 26px; height: 26px; }
  .contact-lines { margin-top: 32px; font-size: 16px; line-height: 1.55; }
  .divider { margin: 22px 0; width: 60px; height: 3px; background: linear-gradient(90deg, var(--green), var(--green-deep)); }
  .location { font-size: 16px; line-height: 1.55; }
</style>
</head>
<body>
  <section class="card front">
    <div class="front-art" role="img" aria-label="Large dark tonal brand emblem illustration"></div>
    <div class="front-wordmark">BrimFalcon</div>
  </section>

  <section class="card back">
    <div class="brand">
      <span class="brand-dot"></span>
      <span class="brand-name">BrimFalcon Labs</span>
    </div>
    <p class="tagline">Precision Built Electric</p>

    <h1 class="person-name">Dana Whitlock</h1>
    <p class="person-title">President &amp; CEO</p>

    <div class="contact-icons">
      <svg viewBox="0 0 26 26" aria-label="Phone"><circle cx="13" cy="13" r="13" fill="#a5ce39"/><path d="M9 7l3 3-1.5 1.5a8 8 0 004 4L16 14l3 3-2 2c-5 0-10-5-10-10z" fill="#2e2e30"/></svg>
      <svg viewBox="0 0 26 26" aria-label="Email"><circle cx="13" cy="13" r="13" fill="#a5ce39"/><rect x="7" y="9" width="12" height="8" fill="#2e2e30"/><path d="M7 9l6 5 6-5" stroke="#a5ce39" stroke-width="1.2" fill="none"/></svg>
      <svg viewBox="0 0 26 26" aria-label="Website"><circle cx="13" cy="13" r="13" fill="#a5ce39"/><circle cx="13" cy="13" r="6.5" fill="none" stroke="#2e2e30" stroke-width="1.6"/><path d="M6.5 13h13M13 6.5c-3 3.5-3 9.5 0 13M13 6.5c3 3.5 3 9.5 0 13" stroke="#2e2e30" stroke-width="1.2" fill="none"/></svg>
    </div>

    <div class="contact-lines">
      <p>555.010.0148</p>
      <p>Dana@BrimFalcon.com</p>
      <p>BrimFalconLabs.com</p>
    </div>
    <div class="divider"></div>
    <div class="location">
      <p>Northvale, Westmark County</p>
      <p>Canada</p>
    </div>
  </section>
</body>
</html>
```